Snack package design "Lantern Curl Bites"

Looking to create a fun package design of snack. Snack is sweet and crunchy; great for people that wants to munch on stuff. Name of the Snack is "Lantern Curl Bites". The net weight should be 16oz (453 grams). I added brand "TWbR" Tiny Wonders bring Rain on the file. I also added picture of the snack. Package will be a pouch type.

Target Market(s)

People that like sweet snacks

Industry/Entity Type

Food snacks

Requirements
Must have
• Name of Snack "Lantern Curl Bites" and logo of company on top left.
Nice to have
• something that's simple and clean design

```html
<!DOCTYPE html>
<html lang="en">
<head>
<meta charset="utf-8">
<title>Lantern Curl Bites – Snack Pouch</title>
<link rel="stylesheet" href="https://fonts.googleapis.com/css2?family=Bangers&family=Fredoka:wght@500;700&family=Cabin:wght@500;700&display=swap">
<style>
  :root {
    --backdrop: #bfbfbf;
    --seal-yellow: #f2c81c;
    --seal-orange: #eda21e;
    --body-yellow: #f5e33a;
    --body-cream: #f4f1dc;
    --new-red: #c8202c;
    --title-black: #111111;
    --title-red: #a3191f;
    --brand-green: #5e9a2c;
    --leaf-green: #4f9a35;
    --deep-green: #0f6a34;
    --snack-light: #e9b86a;
    --snack-mid: #d98b3a;
    --snack-dark: #b8632a;
    --badge-orange: #e0621c;
    --badge-amber: #f2a81e;
    --white: #ffffff;
  }
  * { margin: 0; padding: 0; box-sizing: border-box; }
  html, body { width: 1200px; height: 800px; overflow: hidden; }
  body { background: var(--backdrop); position: relative; font-family: "Cabin", sans-serif; }

  .pouch {
    position: absolute; left: 375px; top: 104px;
    width: 450px; height: 592px; overflow: hidden;
  }
  .pouch-art, .snack-photo { position: absolute; left: 0; top: 0; width: 450px; height: 592px; }

  .tagline {
    position: absolute; top: 62px; left: 0; width: 428px; text-align: center;
    font-family: "Cabin", sans-serif; font-weight: 500; font-size: 17px;
    color: var(--brand-green); white-space: nowrap;
  }
  .brand {
    position: absolute; top: 88px; left: 0; width: 428px;
    display: flex; justify-content: center; align-items: center; gap: 8px;
  }
  .brand-dot { width: 20px; height: 20px; border-radius: 50%; background: var(--new-red); }
  .brand-name {
    font-family: "Fredoka", sans-serif; font-weight: 700; font-size: 40px;
    letter-spacing: 4px; color: var(--brand-green); line-height: 1;
  }

  .new-flag {
    position: absolute; top: 24px; right: 16px;
    font-family: "Bangers", sans-serif; font-size: 28px; letter-spacing: 1px;
    color: var(--white); transform: rotate(-4deg);
  }

  .product-name {
    position: absolute; top: 152px; left: 0; width: 450px; text-align: center;
    font-family: "Bangers", sans-serif; font-weight: 400; line-height: 0.9;
    color: var(--title-black); transform: rotate(-3deg);
  }
  .product-name .line-big { display: block; font-size: 70px; letter-spacing: 1px; }
  .product-name .line-small { display: block; font-size: 30px; color: var(--title-red); margin: 2px 0 2px; }

  .flavor-badge {
    position: absolute; left: 258px; top: 392px; width: 98px; height: 68px;
    text-align: center; color: var(--white);
  }
  .flavor-badge .flavor-name {
    display: block; padding-top: 14px;
    font-family: "Fredoka", sans-serif; font-weight: 700; font-size: 21px; line-height: 1;
  }
  .flavor-badge .flavor-sub {
    display: block; text-align: right; padding-right: 12px;
    font-family: "Cabin", sans-serif; font-weight: 500; font-size: 9px;
  }

  .net-weight {
    position: absolute; left: 72px; top: 490px; color: var(--white);
    font-family: "Fredoka", sans-serif; font-weight: 500; line-height: 1;
  }
  .net-weight .net-label { display: block; font-size: 14px; }
  .net-weight .net-value { display: block; font-size: 30px; }
  .net-weight .net-unit { font-size: 16px; }

  .nutrition {
    position: absolute; left: 272px; top: 492px; display: flex; gap: 3px;
  }
  .nutrient {
    width: 23px; height: 38px; border: 1.5px solid var(--white); border-radius: 4px 4px 3px 3px;
    color: var(--white); text-align: center; line-height: 1; font-family: "Cabin", sans-serif;
  }
  .nutrient .amount { display: block; font-size: 5.5px; font-weight: 700; padding: 3px 0 2px; background: var(--deep-green); border-radius: 50% 50% 0 0; }
  .nutrient .label { display: block; font-size: 3.6px; font-weight: 700; background: var(--white); color: var(--deep-green); padding: 3px 0; }
  .nutrient .percent { display: block; font-size: 6.5px; font-weight: 700; padding-top: 3px; }
</style>
</head>
<body>
  <div class="pouch">
    <svg class="pouch-art" viewBox="0 0 450 592" aria-hidden="true">
      <defs>
        <linearGradient id="bodyFill" x1="0" y1="0" x2="0" y2="1">
          <stop offset="0" stop-color="var(--body-yellow)"/>
          <stop offset="0.35" stop-color="var(--body-cream)"/>
          <stop offset="1" stop-color="var(--body-cream)"/>
        </linearGradient>
        <linearGradient id="sealTop" x1="0" y1="0" x2="1" y2="0">
          <stop offset="0" stop-color="var(--seal-orange)"/>
          <stop offset="0.5" stop-color="var(--seal-yellow)"/>
          <stop offset="1" stop-color="var(--seal-yellow)"/>
        </linearGradient>
        <linearGradient id="greenFill" x1="0" y1="0" x2="0" y2="1">
          <stop offset="0" stop-color="var(--leaf-green)"/>
          <stop offset="0.5" stop-color="var(--deep-green)"/>
          <stop offset="1" stop-color="var(--deep-green)"/>
        </linearGradient>
      </defs>
      <rect class="pouch-body" x="0" y="0" width="450" height="592" fill="url(#bodyFill)"/>
      <rect class="top-seal" x="0" y="0" width="450" height="46" fill="url(#sealTop)"/>
      <g class="seal-ridges" stroke="#ffffff" stroke-opacity="0.35" stroke-width="1">
        <line x1="0" y1="10" x2="450" y2="10"/><line x1="0" y1="36" x2="450" y2="36"/>
      </g>
      <rect class="hang-slot" x="194" y="18" width="54" height="11" rx="5.5" fill="#ffffff" fill-opacity="0.55"/>
      <path class="new-corner" d="M344 0 H450 V54 C430 70 400 80 378 78 C358 76 344 60 344 40 Z" fill="var(--new-red)"/>
    </svg>

    <svg class="snack-photo" viewBox="0 0 450 592" role="img" aria-label="Photo of golden sweet crunchy curl snacks piled up, with a close-up bubble of the bites">
      <defs>
        <linearGradient id="snackPile" x1="0" y1="0" x2="0" y2="1">
          <stop offset="0" stop-color="var(--snack-light)" stop-opacity="0"/>
          <stop offset="0.25" stop-color="var(--snack-light)"/>
          <stop offset="1" stop-color="var(--snack-mid)"/>
        </linearGradient>
        <radialGradient id="snackClose" cx="0.5" cy="0.5" r="0.6">
          <stop offset="0" stop-color="var(--snack-mid)"/>
          <stop offset="1" stop-color="var(--snack-dark)"/>
        </radialGradient>
      </defs>
      <path d="M0 330 C80 300 150 280 220 270 C290 255 380 250 450 250 V560 H0 Z" fill="url(#snackPile)"/>
    </svg>

    <svg class="pouch-art" viewBox="0 0 450 592" aria-hidden="true">
      <path class="green-wave" d="M0 512 C40 470 120 450 220 455 C320 460 400 470 450 472 V592 H0 Z" fill="url(#greenFill)"/>
      <ellipse class="photo-bubble" cx="182" cy="425" rx="78" ry="56" fill="url(#snackClose)" stroke="var(--white)" stroke-width="2" role="img" aria-label="Close-up photo of the curl bites"/>
      <path class="flavor-blob" d="M262 420 C262 396 290 388 318 390 C346 392 358 410 356 430 C354 452 330 462 300 460 C272 458 262 444 262 420 Z" fill="var(--badge-orange)" stroke="var(--white)" stroke-width="2"/>
      <path d="M264 432 C280 448 330 452 354 436 C350 452 330 460 300 459 C276 458 266 448 264 432 Z" fill="var(--badge-amber)"/>
      <rect class="bottom-seal" x="0" y="558" width="450" height="34" fill="var(--deep-green)"/>
      <g stroke="#ffffff" stroke-opacity="0.2" stroke-width="1">
        <line x1="0" y1="568" x2="450" y2="568"/><line x1="0" y1="582" x2="450" y2="582"/>
      </g>
    </svg>

    <p class="tagline">Tiny Wonders bring Rain</p>
    <div class="brand">
      <span class="brand-name">TWbR</span>
      <span class="brand-dot"></span>
    </div>
    <p class="new-flag">New!</p>

    <h1 class="product-name">
      <span class="line-big">Lantern</span>
      <span class="line-small">Curl</span>
      <span class="line-big">Bites</span>
    </h1>

    <div class="flavor-badge">
      <span class="flavor-name">Original</span>
      <span class="flavor-sub">Flavor</span>
    </div>

    <div class="net-weight">
      <span class="net-label">Net</span>
      <span class="net-value">453<span class="net-unit">g</span></span>
    </div>

    <div class="nutrition">
      <div class="nutrient"><span class="amount">550</span><span class="label">Calories</span><span class="percent">20%</span></div>
      <div class="nutrient"><span class="amount">0.5g</span><span class="label">Salt</span><span class="percent">4%</span></div>
      <div class="nutrient"><span class="amount">24.8g</span><span class="label">Fat</span><span class="percent">34%</span></div>
      <div class="nutrient"><span class="amount">6.1g</span><span class="label">Saturates</span><span class="percent">7%</span></div>
      <div class="nutrient"><span class="amount">7.3g</span><span class="label">Sugars</span><span class="percent">8%</span></div>
    </div>
  </div>
</body>
</html>
```